Business Card Design REAL ESTATE SALES PLEASE DESIGN MY CARD 2COLOR CARD WITH RED AS THE DOMINANT

MOOR PINE REALTY
TorVHA Lic# 04827316
WALTER " WALT " KOVIC Tel 510 555-0142
TorVHA Lic# 00762408 Fax 510 555-0187
Email: walt@waltkovic.example Cell 510 555-0163
48610 FERNHILL COURT UNION CITY, CA 94999

Business

WALTER " WALT " KOVIC
TEL: 510 555-0142 FAX 510 555-0187
Address: 48610 Fernhill Court Union City , CA
EMAIL ADDRESS: walt@waltkovic.example

```html
<!DOCTYPE html>
<html lang="en">
<head>
<meta charset="utf-8">
<title>Moor Pine Realty – Business Card</title>
<link href="https://fonts.googleapis.com/css2?family=Open+Sans:wght@400;700&display=swap" rel="stylesheet">
<style>
  :root {
    --page: #e9e6e1;
    --card-dark: #2f2f31;
    --card-red: #d61f27;
    --brand-red: #e0252d;
    --white: #ffffff;
    --dot-light: #e2e2e2;
    --dot-mid: #a9161d;
    --dot-dark: #2a2a2a;
  }
  * { margin: 0; padding: 0; box-sizing: border-box; }
  html, body {
    width: 1200px; height: 1023px; overflow: hidden;
    background: var(--page);
  }
  .canvas {
    width: 1200px; height: 1023px;
    display: flex; flex-direction: column; align-items: center; justify-content: center;
    gap: 24px;
  }
  .card {
    width: 840px; height: 480px; position: relative;
    box-shadow: 0 6px 18px rgba(0,0,0,.18);
  }
  /* Front */
  .card-front {
    background: var(--card-dark);
    font-family: "Open Sans", sans-serif; color: var(--brand-red);
  }
  .brand-block {
    position: absolute; left: 230px; top: 190px; width: 500px;
  }
  .brand-line { display: flex; align-items: center; gap: 18px; }
  .brand-square { width: 34px; height: 34px; background: var(--brand-red); flex: none; }
  .brand-name {
    font-size: 46px; font-weight: 700; letter-spacing: 1px; line-height: 1;
  }
  .licenses {
    display: flex; justify-content: space-between;
    margin-top: 22px; padding-left: 52px; font-size: 17px; font-weight: 700;
  }
  /* Back */
  .card-back {
    background: var(--card-red); color: var(--white);
    font-family: "Open Sans", sans-serif; padding: 60px 64px;
  }
  .agent-name { font-size: 44px; font-weight: 700; letter-spacing: 1px; margin-bottom: 8px; }
  .agent-license { font-size: 20px; margin-bottom: 40px; }
  .contact-list { list-style: none; display: flex; flex-direction: column; gap: 22px; }
  .contact-item { display: flex; align-items: center; gap: 22px; font-size: 22px; }
  .contact-item svg { width: 30px; height: 30px; flex: none; }
  .dots { position: absolute; right: 70px; bottom: 70px; display: flex; flex-direction: column; gap: 6px; }
  .dot { width: 30px; height: 30px; border-radius: 50%; }
  .dot-light { background: var(--dot-light); }
  .dot-mid { background: var(--dot-mid); margin-left: 16px; }
  .dot-dark { background: var(--dot-dark); margin-left: 32px; }
</style>
</head>
<body>
<main class="canvas">
  <section class="card card-front">
    <div class="brand-block">
      <div class="brand-line">
        <span class="brand-square" aria-hidden="true"></span>
        <h1 class="brand-name">MOOR PINE REALTY</h1>
      </div>
      <div class="licenses">
        <span>TorVHA Lic# 04827316</span>
        <span>TorVHA Lic# 00762408</span>
      </div>
    </div>
  </section>

  <section class="card card-back">
    <h2 class="agent-name">WALTER " WALT " KOVIC</h2>
    <p class="agent-license">TorVHA Lic# 00762408</p>
    <ul class="contact-list">
      <li class="contact-item">
        <svg viewBox="0 0 24 24" aria-hidden="true"><path fill="#fff" d="M6.6 10.8a15 15 0 0 0 6.6 6.6l2.2-2.2a1 1 0 0 1 1-.25 11.4 11.4 0 0 0 3.6.57 1 1 0 0 1 1 1V20a1 1 0 0 1-1 1A17 17 0 0 1 3 4a1 1 0 0 1 1-1h3.5a1 1 0 0 1 1 1c0 1.25.2 2.45.57 3.6a1 1 0 0 1-.25 1z"/></svg>
        <span>Tel 510 555-0142 &nbsp; Fax 510 555-0187 &nbsp; Cell 510 555-0163</span>
      </li>
      <li class="contact-item">
        <svg viewBox="0 0 24 24" aria-hidden="true"><rect x="2" y="5" width="20" height="14" fill="none" stroke="#fff" stroke-width="2"/><path d="M2 5l10 8 10-8" fill="none" stroke="#fff" stroke-width="2"/></svg>
        <span>walt@waltkovic.example</span>
      </li>
      <li class="contact-item">
        <svg viewBox="0 0 24 24" aria-hidden="true"><path fill="#fff" d="M12 2a7 7 0 0 0-7 7c0 5 7 13 7 13s7-8 7-13a7 7 0 0 0-7-7zm0 9.5A2.5 2.5 0 1 1 12 6.5a2.5 2.5 0 0 1 0 5z"/></svg>
        <span>48610 FERNHILL COURT UNION CITY, CA 94999</span>
      </li>
    </ul>
    <div class="dots" aria-hidden="true">
      <span class="dot dot-light"></span>
      <span class="dot dot-mid"></span>
      <span class="dot dot-dark"></span>
    </div>
  </section>
</main>
</body>
</html>
```